tourism marketplace web app redesign*

Hi, I need our front-page redesigned. For the competition please submit a jpg of ABOVE THE FOLD ONLY. The full page redesign will be a revision request. URL is https://qp.trolvexa.hu/hu/index.html login:'fullhd' and password:'asdasd' (Fold is supposed to be at "Kiemelt Ajanlatok", use all elements above that. Please use at least one extra color other than the two in the logo, or you may completely change them. FOCUS should be on the central combined search box (3 dropdown, 2 calendar picker + Kereses Button) just like nestorly.com, ravimoto.com, Pelusi.com, etc... The search box is always large, central, white, we want that too. We want it to look more modern, more clean AND we want to feature a changing beautiful nature photo background (like nestorly.com).Please use our newly designed logo (in attached pdf) and use that new spelling: "ferntrail.online"

```html
<!DOCTYPE html>
<html lang="hu">
<head>
<meta charset="utf-8">
<title>ferntrail.online</title>
<link href="https://fonts.googleapis.com/css2?family=Roboto:wght@400;500;700&display=swap" rel="stylesheet">
<style>
:root{
  --teal:#6aab9c;
  --teal-light:#7cbdb3;
  --ink:#222;
  --muted:#777;
  --field:#f7f7fc;
  --line:#e4e4ee;
  --footer:#232323;
  --white:#fff;
}
*{box-sizing:border-box;margin:0;padding:0}
html,body{width:868px;height:1200px;overflow:hidden;background:var(--white);font-family:"Roboto",sans-serif;color:var(--ink)}
.page{position:relative;width:868px;height:1200px}
.hero{position:absolute;left:0;top:0;width:868px;height:453px;
  background:
   linear-gradient(90deg,rgba(30,55,35,.85) 0%,rgba(40,70,45,.35) 25%,rgba(0,0,0,0) 40%,rgba(0,0,0,0) 60%,rgba(30,50,30,.6) 80%,rgba(25,45,25,.9) 100%),
   linear-gradient(180deg,#c9cfd0 0%,#a9b4b0 30%,#5f7d63 55%,#4a6f52 75%,#6c8d78 100%);}
.topbar{position:absolute;left:0;top:0;width:868px;height:56px;background:rgba(120,120,120,.35)}
.brand{position:absolute;display:flex;align-items:center;gap:7px;color:var(--white);font-weight:500;font-size:17px;white-space:nowrap}
.brand .dot{width:42px;height:42px;border-radius:50%;background:var(--teal)}
.brand.top{left:63px;top:7px}
.nav{position:absolute;top:26px;font-size:9.5px;font-weight:700;color:var(--white);letter-spacing:.2px}
.partner{position:absolute;left:680px;top:20px;width:97px;height:19px;background:var(--teal);color:var(--white);font-size:9px;display:flex;align-items:center;justify-content:center;gap:3px;white-space:nowrap}

.tagline{position:absolute;left:0;top:118px;width:868px;text-align:center;color:var(--white)}
.tagline h1{font-size:26px;font-weight:500;text-shadow:0 1px 6px rgba(0,0,0,.35)}
.tagline p{font-size:9.5px;font-weight:700;letter-spacing:1.6px;margin-top:8px;text-shadow:0 1px 4px rgba(0,0,0,.35)}
.cats{position:absolute;left:0;top:200px;width:868px;display:flex;justify-content:center;gap:4px}
.cat{height:21px;padding:0 10px;background:var(--teal-light);color:var(--white);font-size:9px;display:flex;align-items:center;white-space:nowrap}

.search{position:absolute;left:54px;top:286px;width:760px;height:170px;background:var(--white);border-radius:6px;box-shadow:0 14px 36px rgba(0,0,0,.22);padding:24px 26px}
.search h2{font-size:15px;font-weight:500;text-align:center}
.fields{display:flex;align-items:center;gap:8px;margin-top:22px}
.select{position:relative;flex:0 0 124px;height:44px;background:var(--field);border:1px solid var(--line);font-size:10px;color:#999;padding-left:12px;display:flex;align-items:center;white-space:nowrap}
.select::after{content:"";position:absolute;right:11px;top:19px;border:3.5px solid transparent;border-top:4px solid #555}
.date{flex:0 0 96px;height:44px;border:1px solid #ccc;border-radius:2px;font-size:11px;padding-left:10px;display:flex;align-items:center;color:#333}
.swap{flex:0 0 10px}
.go{flex:1 1 auto;height:44px;background:var(--teal);color:var(--white);font-weight:500;font-size:13px;display:flex;align-items:center;justify-content:center;gap:5px}

.featured{position:absolute;top:500px;width:868px;text-align:center}
.featured h2{color:var(--teal-light);font-size:23.5px;font-weight:500}
.featured p{font-size:8.5px;color:#555;margin-top:9px}
.card{position:absolute;top:596px;width:364px;height:440px;border:1px solid #555;border-radius:6px;text-align:center}
.card .photo{position:absolute;top:30px;height:197px}
.card h3{position:absolute;top:245px;width:100%;color:var(--teal-light);font-size:15px;font-weight:500}
.card h4{position:absolute;top:269px;width:100%;color:#666;font-size:15px;font-weight:500}
.card p{position:absolute;top:292px;left:16px;right:16px;font-size:9.2px;line-height:16px;color:#888}
.more{position:absolute;top:374px;left:150px;width:62px;height:20px;background:var(--teal);color:var(--white);font-size:8.5px;display:flex;align-items:center;justify-content:center;gap:2px}
.stars{position:absolute;top:397px;left:0;width:100%;display:flex;justify-content:center}
.dots{position:absolute;left:846px;width:9px;height:9px;background:#eee}
.dots.on{background:var(--teal)}
.footer{position:absolute;left:0;top:1076px;width:868px;height:124px;background:var(--footer)}
.brand.bottom{left:347px;top:48px;font-size:19px}
.copy{position:absolute;top:94px;width:100%;text-align:center;font-size:8.5px;color:#888}
</style>
</head>
<body>
<div class="page">
  <div class="hero" role="img" aria-label="Fenyőerdős hegyi tó tükröződő vízzel, háttérben ködös sziklás csúcsok"></div>
  <div class="topbar"></div>
  <div class="brand top"><span class="dot"></span>ferntrail.online</div>
  <span class="nav" style="left:401px">ORSZÁGOK</span>
  <span class="nav" style="left:482px">VADFAJOK</span>
  <span class="nav" style="left:560px">RÓLUNK</span>
  <span class="nav" style="left:627px">ÁSZF</span>
  <div class="partner"><svg width="8" height="8" viewBox="0 0 8 8"><circle cx="4" cy="4" r="4" fill="#fff"/><path d="M4 2v4M2 4h4" stroke="#6aab9c" stroke-width="1.3"/></svg>Legyen partnerünk</div>

  <div class="tagline">
    <h1>Nincs szükséged vadászatszervezőre!</h1>
    <p>FOGLALJ KÖZVETLEN A VADÁSZTERÜLETNÉL</p>
  </div>
  <div class="cats">
    <div class="cat">Egyéni vadászatok</div>
    <div class="cat">Társas vadászatok, hajtások</div>
    <div class="cat">Exkluzív csomagok</div>
  </div>

  <div class="search">
    <h2>Search Properties</h2>
    <div class="fields">
      <div class="select">Összes vad</div>
      <div class="select">Összes ország</div>
      <div class="select">Összes ajánlat</div>
      <div class="date">jj/mm/aaaa</div>
      <svg class="swap" width="10" height="8" viewBox="0 0 10 8"><path d="M1 4h8M3 2L1 4l2 2M7 2l2 2-2 2" stroke="#6aab9c" fill="none"/></svg>
      <div class="date">jj/mm/aaaa</div>
      <div class="go"><svg width="12" height="12" viewBox="0 0 11 11"><circle cx="4.5" cy="4.5" r="3.4" stroke="#fff" stroke-width="1.6" fill="none"/><path d="M7 7l3 3" stroke="#fff" stroke-width="1.8"/></svg>Keresés</div>
    </div>
  </div>

  <div class="featured">
    <h2>Kiemelt ajánlatok</h2>
    <p>További ajánlatok</p>
  </div>

  <div class="card" style="left:63px">
    <div class="photo" role="img" aria-label="Gímszarvas bika füves tisztáson erdő előtt" style="left:29px;width:305px;background:linear-gradient(180deg,#1f3a22 0%,#3f5a2e 45%,#8a7a4a 75%,#b89a62 100%)"></div>
    <h3>Első ajánlat neve</h3>
    <h4>Város neve, Hungary - 1.234 €-tól</h4>
    <p>Lorem ipsum dolor sit amet, consectetur adipiscing elit. Sed velit ipsum, volutpat eget elementum eu, aliquet at elit. Vivamus condimentum ultrices sem, ut luctus mauris tristique sed. Quisque aliquet auctor mauris nec scelerisque.</p>
    <div class="more">Részletek <svg width="8" height="8" viewBox="0 0 8 8"><circle cx="4" cy="4" r="3.5" stroke="#fff" fill="none"/><path d="M2 4h4M4.5 2.5L6 4 4.5 5.5" stroke="#fff" fill="none"/></svg></div>
    <div class="stars">
      <svg width="52" height="9" viewBox="0 0 52 9"><g fill="#7cbdb3"><path id="s" d="M4.5 0l1.1 3h3.1L6.2 5l1 3.2-2.7-2-2.7 2 1-3.2L.3 3h3.1z"/><use href="#s" x="10.5"/><use href="#s" x="21"/><use href="#s" x="31.5"/></g><use href="#s" x="42" fill="none" stroke="#7cbdb3" stroke-width=".7"/></svg>
    </div>
  </div>

  <div class="card" style="left:447px">
    <div class="photo" role="img" aria-label="Legelésző jávorszarvas fenyőerdőben" style="left:35px;width:296px;background:linear-gradient(180deg,#9cc3d8 0%,#3c5a3c 35%,#4e6a3e 65%,#6b7a52 100%)"></div>
    <h3>Első ajánlat neve</h3>
    <h4>Város neve, Hungary - 1.234 €-tól</h4>
    <p>Lorem ipsum dolor sit amet, consectetur adipiscing elit. Sed velit ipsum, volutpat eget elementum eu, aliquet at elit. Vivamus condimentum ultrices sem, ut luctus mauris tristique sed. Quisque aliquet auctor mauris nec scelerisque.</p>
    <div class="more">Részletek <svg width="8" height="8" viewBox="0 0 8 8"><circle cx="4" cy="4" r="3.5" stroke="#fff" fill="none"/><path d="M2 4h4M4.5 2.5L6 4 4.5 5.5" stroke="#fff" fill="none"/></svg></div>
    <div class="stars">
      <svg width="52" height="9" viewBox="0 0 52 9"><g fill="#7cbdb3"><use href="#s"/><use href="#s" x="10.5"/><use href="#s" x="21"/><use href="#s" x="31.5"/></g><use href="#s" x="42" fill="none" stroke="#7cbdb3" stroke-width=".7"/></svg>
    </div>
  </div>

  <div class="dots on" style="top:793px"></div>
  <div class="dots" style="top:809px"></div>
  <div class="dots" style="top:825px"></div>

  <div class="footer">
    <div class="brand bottom"><span class="dot"></span>ferntrail.online</div>
    <div class="copy">© Ferntrail.Online 2018.</div>
  </div>
</div>
</body>
</html>
```